International Food Manufacturer in the need of a new business card and logo.

Our Company - Northgate Pantry Ltd.

Our Industry - Food and Drink

We are a Wild Harvested Food Distributor / Manufacturer. We service the following food sectors: Supermarkets, Hotels, Restaurants, Cafes, Catering and all people looking to eat healthy food products.

Slogan - Your trusted pantry for wholesome living

Business card details -

48-52 Marlow Lane
Hatherby Green
London
EC9Z 4RT United Kingdom
Dennis Prowle
+44 7000 481736 - UK
+971 50 7739205 - UAE
+38 063 914 2758 - Ukraine
dennis@northgatepantry.example
www.northgatepantry.example

Goal - We are looking for a dynamic modern new look for our corporate image and a designer who can bring this new concept to our future food product designs. Please try to incorporate 3d hexagonal vector Imaging in your design concepts.

Target Market(s)

Industry/Entity Type

Food Service

Contact Information for Business Card

Northgate Pantry Ltd.
48-52 Marlow Lane
Hatherby Green
London
EC9Z 4RT United Kingdom
Dennis Prowle
+44 7000 481736 - UK
+971 50 7739205 - UAE

Font styles to use
Serif

Colors

Designer to choose colors to be used in the design.

Requirements
Must have
• Please read project description above.
Nice to have
Should not have

```html
<!DOCTYPE html>
<html lang="en">
<head>
<meta charset="utf-8">
<title>Northgate Pantry Ltd. – Business Card</title>
<link rel="stylesheet" href="https://fonts.googleapis.com/css2?family=Old+Standard+TT&family=Open+Sans:wght@700&family=Questrial&display=swap">
<style>
  :root {
    --paper: #ffffff;
    --navy: #123f8f;
    --ink: #0d3b8c;
    --soft-ink: #1d4c9c;
    --sky: #3a8fdc;
    --facet-light: #7ff0ee;
    --facet-mid: #3fc6ee;
    --facet-deep: #2a8fe0;
    --facet-dark: #0d4595;
    --serif: "Old Standard TT", "Times New Roman", serif;
    --bold-sans: "Open Sans", Arial, sans-serif;
    --light-sans: "Questrial", "Century Gothic", sans-serif;
  }
  html, body {
    margin: 0;
    padding: 0;
    overflow: hidden;
    background: var(--paper);
  }
  .card {
    position: relative;
    width: 1200px;
    height: 777px;
    background: var(--paper);
    overflow: hidden;
  }
  .facet-panel {
    position: absolute;
    left: 0;
    top: 0;
  }
  .brand-mark {
    position: absolute;
    left: 192px;
    top: 40px;
    width: 136px;
    text-align: center;
    color: var(--navy);
    font-family: var(--serif);
    font-size: 22px;
    line-height: 1.2;
  }
  .brand-mark .dot {
    display: block;
    width: 92px;
    height: 92px;
    margin: 0 auto 22px;
    border-radius: 50%;
    background: var(--facet-deep);
  }
  .centered {
    position: absolute;
    left: 0;
    margin: 0;
    text-align: center;
    white-space: nowrap;
    line-height: 1;
  }
  .company-name {
    top: 99px;
    width: 1414px;
    font-family: var(--serif);
    font-weight: 400;
    font-size: 58px;
    color: var(--navy);
  }
  .slogan {
    top: 170px;
    width: 1414px;
    font-family: var(--serif);
    font-size: 32px;
    color: var(--sky);
  }
  .rule {
    position: absolute;
    left: 406px;
    top: 215px;
    width: 602px;
    height: 4px;
    background: var(--navy);
  }
  .contact {
    width: 1256px;
  }
  .person-name {
    top: 261px;
    font-family: var(--serif);
    font-weight: 400;
    font-size: 50px;
    color: var(--navy);
  }
  .phone {
    font-family: var(--bold-sans);
    font-weight: 700;
    font-size: 44px;
    color: var(--ink);
  }
  .phone-uk { top: 334px; }
  .phone-uae { top: 396px; }
  .phone-ua { top: 456px; }
  .line-light {
    font-family: var(--light-sans);
    color: var(--soft-ink);
  }
  .email { top: 543px; font-size: 47px; }
  .web { top: 603px; font-size: 47px; }
  .address-1 { top: 662px; font-size: 44px; }
  .address-2 { top: 709px; font-size: 44px; }
</style>
</head>
<body>
<div class="card">
  <svg class="facet-panel" width="270" height="777" viewBox="0 0 270 777" role="img" aria-label="Faceted blue low-poly hexagonal decoration along the left edge">
    <defs>
      <linearGradient id="facetFill" x1="0" y1="0" x2="0.4" y2="1">
        <stop offset="0" stop-color="var(--facet-mid)"/>
        <stop offset="0.3" stop-color="var(--facet-light)"/>
        <stop offset="0.6" stop-color="var(--facet-mid)"/>
        <stop offset="0.82" stop-color="var(--facet-deep)"/>
        <stop offset="1" stop-color="var(--facet-dark)"/>
      </linearGradient>
    </defs>
    <polygon points="0,0 66,0 254,386 90,777 0,777" fill="url(#facetFill)"/>
  </svg>

  <div class="brand-mark">
    <span class="dot"></span>
    Northgate Pantry
  </div>

  <h1 class="centered company-name">Northgate Pantry Ltd.</h1>
  <p class="centered slogan">Your trusted pantry for wholesome living</p>
  <div class="rule"></div>

  <h2 class="centered contact person-name">Dennis Prowle</h2>
  <p class="centered contact phone phone-uk">+44 7000 481736 - UK</p>
  <p class="centered contact phone phone-uae">+971 50 7739205 - UAE</p>
  <p class="centered contact phone phone-ua">+38 063 914 2758 - Ukraine</p>

  <p class="centered contact line-light email">dennis@northgatepantry.example</p>
  <p class="centered contact line-light web">www.northgatepantry.example</p>
  <p class="centered contact line-light address-1">48-52 Marlow Lane Hatherby Green London</p>
  <p class="centered contact line-light address-2">EC9Z 4RT United Kingdom</p>
</div>
</body>
</html>
```